Design and Renovation Company Luxury Business Card

I want to create a luxury business card for a Design and Renovation Firm . We will use our current logo. The company name is 742BUILD. We do not want anything standard. We need a very unique concept.
Please see uploaded inspiration. I really like the textured paper option. I would like the card to be thick with debossing, and/or embossing options. The logo has orange in it but I would like to see the card with and without the orange. I think the orange may make the company feel less high-end. The goal is to elevate the logo not match its vibe per se of the logo. We want something very unique, not standard at all!
I would like a space for :
Logo,
Name,
Position,
Email,
Office number,
Website Address,
Business Address,
Thank you!
Have fun!
Target Market(s)
Home owners Age 35 +
Industry/Entity Type
Design and Renovation
Contact Information for Business Card
Logo, Name, Position, Email, Office number, Website Address, Business Address,.
Colors
Designer to choose colors to be used in the design.
Requirements
Must have
- A luxury designer feel. Must be black or dark grey but open to other luxury ideas.
Nice to have
- Gold, silver, black embossing or debossing. Textured paper design.
Should not have
- A cheap look and feel.

```html
<!DOCTYPE html>
<html lang="en">
<head>
<meta charset="utf-8">
<title>742BUILD Business Card</title>
<link href="https://fonts.googleapis.com/css2?family=Montserrat:wght@400;500;700&display=swap" rel="stylesheet">
<style>
  :root {
    --backdrop: #d1d6d5;
    --paper: #f1f1ef;
    --ink: #141414;
    --grey: #3a3a3a;
    --accent: #f7941d;
  }
  html, body {
    margin: 0;
    width: 1200px;
    height: 881px;
    overflow: hidden;
    background: var(--backdrop);
    font-family: "Montserrat", sans-serif;
  }
  .canvas {
    width: 1200px;
    height: 881px;
    display: flex;
    align-items: center;
    justify-content: center;
    gap: 40px;
  }
  .card {
    position: relative;
    width: 540px;
    height: 309px;
    background: var(--paper);
    border-bottom: 5px solid var(--accent);
    box-sizing: border-box;
    box-shadow: 0 10px 24px rgba(0,0,0,0.12);
  }
  .brand-name {
    font-weight: 700;
    color: var(--ink);
    letter-spacing: 0.04em;
    line-height: 1;
    white-space: nowrap;
  }
  /* front: contact side */
  .card--contact {
    display: flex;
    align-items: center;
  }
  .card--contact .brand-name {
    width: 230px;
    margin-left: 40px;
    font-size: 30px;
  }
  .divider {
    width: 2px;
    height: 120px;
    background: var(--accent);
    margin: 0 24px 0 12px;
  }
  .contact__name {
    margin: 0;
    font-size: 19px;
    font-weight: 700;
    color: var(--accent);
    letter-spacing: 0.02em;
  }
  .contact__role {
    margin: 2px 0 10px;
    font-size: 11px;
    color: var(--grey);
  }
  .contact__address {
    margin: 0 0 8px;
    font-size: 10.5px;
    color: var(--grey);
    line-height: 1.4;
    font-style: normal;
  }
  .contact__list {
    list-style: none;
    margin: 0;
    padding: 0;
    font-size: 10.5px;
    color: var(--grey);
  }
  .contact__list li {
    display: flex;
    align-items: center;
    gap: 6px;
    line-height: 1.7;
  }
  .contact__list svg { width: 10px; height: 10px; flex: none; }
  /* back: brand side */
  .card--brand {
    display: flex;
    align-items: center;
    justify-content: center;
  }
  .card--brand .brand-name { font-size: 60px; }
</style>
</head>
<body>
<main class="canvas">
  <section class="card card--contact">
    <span class="brand-name">742BUILD</span>
    <span class="divider"></span>
    <div class="contact">
      <h1 class="contact__name">DANIEL HART</h1>
      <p class="contact__role">Managing Director</p>
      <address class="contact__address">18 Alder Lane, Fairview<br>OR, 97001</address>
      <ul class="contact__list">
        <li>
          <svg viewBox="0 0 10 10" aria-hidden="true"><path d="M2 1h2l1 2.5-1.2.8a5 5 0 0 0 1.9 1.9l.8-1.2L9 6v2a1 1 0 0 1-1 1A7 7 0 0 1 1 2a1 1 0 0 1 1-1z" fill="var(--accent)"/></svg>
          555 204 318
        </li>
        <li>
          <svg viewBox="0 0 10 10" aria-hidden="true"><rect x="0.5" y="2" width="9" height="6" rx="1" fill="var(--accent)"/><path d="M1 2.6 5 5.4l4-2.8" stroke="var(--paper)" stroke-width="0.8" fill="none"/></svg>
          hello@742build.com
        </li>
        <li>
          <svg viewBox="0 0 10 10" aria-hidden="true"><circle cx="5" cy="5" r="4.3" fill="none" stroke="var(--accent)" stroke-width="1.2"/><path d="M0.8 5h8.4M5 0.8c-2.2 2.5-2.2 5.9 0 8.4M5 0.8c2.2 2.5 2.2 5.9 0 8.4" stroke="var(--accent)" stroke-width="0.8" fill="none"/></svg>
          www.742build.com
        </li>
      </ul>
    </div>
  </section>

  <section class="card card--brand">
    <span class="brand-name">742BUILD</span>
  </section>
</main>
</body>
</html>
```